Website design to promote trampoline business

We require a website design for our business. The business is primarily provising access for people between 5YO and 40YO to jump on trampolines for fun and fitness.

We have a logo and color schemes already and the website should incorporate these colors and designs.

We would like to incorporate the following pages:-

Book Now!
Home
About Us
Locations & Hours
Jumping
Groups & Events
Gallery
Safety
Latest News
Careers

Industry/Entity Type

Business

Requirements
Must have
• Incorporate our logo and colors (files attached).

```html
<!DOCTYPE html>
<html lang="en">
<head>
<meta charset="utf-8">
<title>Hoply Trampolines</title>
<link href="https://fonts.googleapis.com/css2?family=Open+Sans:wght@400;600;700&family=Open+Sans+Condensed:wght@300;700&display=swap" rel="stylesheet">
<style>
:root{
  --orange:#ff7f00;
  --orange-dark:#c85f00;
  --blue:#00a0d8;
  --blue-dark:#0079a8;
  --grey:#a0a0a0;
  --grey-dark:#777;
  --text:#333;
  --muted:#666;
  --line:#dcdcdc;
  --header-bg:#f2f2f2;
  --nav-top:#9a9ea3;
  --nav-bot:#6f7479;
}
*{box-sizing:border-box;margin:0;padding:0}
html,body{width:1068px;height:1200px;overflow:hidden;background:#fff;font-family:"Open Sans",sans-serif;color:var(--text)}
.page{position:relative;width:1068px;height:1200px}
.abs{position:absolute}
.topline{left:0;top:0;width:1068px;height:4px;background:#a8a8a8}
.header{left:0;top:4px;width:1068px;height:90px;background:var(--header-bg);border-bottom:1px solid var(--line)}
.brand{left:162px;top:18px;display:flex;align-items:center;gap:8px;font-weight:700;font-size:40px;color:var(--orange);letter-spacing:1px}
.brand-dot{width:14px;height:14px;background:var(--blue)}
.brand-sub{left:166px;top:64px;font-size:11px;color:var(--grey-dark);letter-spacing:2px}
.call{left:398px;top:36px;display:flex;gap:6px;align-items:center;font-size:10.5px;line-height:12px;color:#333}
.lang{left:534px;top:42px;font-size:11px;display:flex;align-items:center;gap:6px}
.flag{width:19px;height:13px;background:linear-gradient(#2a3f8f,#2a3f8f);position:relative;overflow:hidden}
.flag:before{content:"";position:absolute;left:7px;top:0;width:5px;height:13px;background:#fff;border-left:1.5px solid #c8102e;border-right:1.5px solid #c8102e}
.flag:after{content:"";position:absolute;left:0;top:4px;width:19px;height:5px;background:#c8102e;border-top:1.5px solid #fff;border-bottom:1.5px solid #fff}
.sep{width:1px;height:14px;background:#ccc;margin:0 8px}
.btn-sm{top:41px;height:16px;border-radius:4px;background:linear-gradient(#a9adb1,#7f8489);color:#fff;font-size:9.5px;text-align:center;line-height:16px}
.search{left:806px;top:41px;width:100px;height:16px;border-radius:4px;background:linear-gradient(#a9adb1,#7f8489);color:#eee;font-size:8px;line-height:16px;padding-left:7px}
.search svg{position:absolute;right:6px;top:3px}
.nav{left:162px;top:94px;width:744px;height:29px;background:linear-gradient(var(--nav-top),var(--nav-bot));display:flex;justify-content:space-around;align-items:center;padding:0 4px;border-radius:0 0 3px 3px}
.nav a{color:#fff;text-decoration:none;font-family:"Open Sans Condensed",sans-serif;font-weight:700;font-size:11.5px;letter-spacing:-.2px}
.side-head{left:162px;width:154px;height:28px;border-radius:3px;background:linear-gradient(#a9adb1,#7f8489);color:#fff;font-family:"Open Sans Condensed",sans-serif;font-weight:700;font-size:15px;text-align:center;line-height:28px}
.side-box{left:162px;width:154px;border:1px solid #d6d6d6;box-shadow:0 1px 2px rgba(0,0,0,.1);background:#fff}
.cal-title{text-align:center;font-size:11px;color:var(--muted);padding-top:10px;position:relative}
.cal-title span{position:absolute;top:10px;font-size:8px;color:#999}
.cal{width:142px;margin:14px auto 0;border-collapse:collapse}
.cal th{font-size:5.5px;color:#e25050;font-weight:700;height:10px}
.cal td{font-size:7.5px;text-align:center;height:17.5px;color:#444}
.cal td.o{color:#aaa}
.basket{font-size:9.5px;color:#555;padding:10px 12px}
.area{font-size:8.7px;line-height:12.2px;color:#555;text-align:justify;padding:9px 11px}
.view-map{display:block;margin:13px auto 0;width:72px;height:21px;background:linear-gradient(#a9adb1,#7f8489);color:#fff;font-size:10px;text-align:center;line-height:21px;border-radius:2px}
.slider{left:329px;top:150px;width:577px;height:230px;border:1px solid #d6d6d6;background:linear-gradient(90deg,#e6e6e6,#fbfbfb 50%,#f0f0f0);overflow:hidden}
.slider-art{position:absolute;left:40px;top:6px;width:210px;height:220px;background:radial-gradient(ellipse at 50% 45%,#4a4f55,#8a9096 60%,rgba(200,200,200,0) 75%)}
.tag{position:absolute;font-weight:600;letter-spacing:-1.5px;line-height:1}
.tag1{left:232px;top:47px;background:var(--orange);color:#111;font-size:31px;padding:8px 22px 6px 15px}
.tag1 b{color:#fff;font-weight:600}
.tag2{left:233px;top:96px;background:var(--blue);color:#111;font-size:31px;padding:5px 12px 8px 8px}
.tag2 b{color:#fff;font-weight:600}
.tag3{left:220px;top:138px;background:#a8a8a8;color:#111;font-size:26px;padding:8px 13px 8px 22px}
.arrow{position:absolute;top:107px;width:25px;height:25px;border-radius:50%;background:#a3a3a3;display:flex;align-items:center;justify-content:center}
.dots{position:absolute;left:263px;top:206px;display:flex;gap:6px}
.dots i{width:11px;height:11px;border-radius:50%;border:1px solid #bbb;background:#fff}
.dots i.on{background:#444}
.toolbar{left:329px;top:394px;width:577px;height:16px;font-size:9.5px;color:#555;display:flex;align-items:center}
.pager{display:flex;margin-left:12px}
.pager span{width:18.5px;height:15px;border:1px solid #ccc;margin-left:-1px;font-size:9px;text-align:center;line-height:13px}
.pager .cur{color:var(--blue)}
.sort{margin-left:74px;color:var(--blue)}
.select{margin-left:4px;width:108px;height:15px;border:1px solid #ccc;font-size:9px;color:#444;padding-left:7px;line-height:13px;position:relative}
.select:after{content:"";position:absolute;right:5px;top:3px;width:4px;height:4px;border-right:1px solid #666;border-bottom:1px solid #666;transform:rotate(45deg)}
.toggle{margin-left:auto;display:flex;align-items:center;gap:8px;color:var(--blue)}
.track{width:70px;height:6px;border-radius:3px;background:#ddd;position:relative}
.track i{position:absolute;left:9px;top:-4px;width:14px;height:14px;border-radius:50%;background:#fff;box-shadow:0 1px 2px rgba(0,0,0,.3)}
.track i:after{content:"";position:absolute;left:5px;top:5px;width:4px;height:4px;border-radius:50%;background:var(--blue)}
.product{left:329px;width:577px;height:85px}
.product-rule{left:329px;width:577px;height:1px;background:var(--line)}
.thumb{position:absolute;left:0;top:0;width:97px;height:85px;border:1px solid #ccc;background:#fff;padding:6px}
.thumb div{width:100%;height:100%;background:radial-gradient(ellipse at 50% 50%,#56606a,#a9b3bb 55%,#fff 75%)}
.p-name{position:absolute;left:112px;top:5px;font-size:10.5px;font-weight:600;color:#222}
.p-desc{position:absolute;left:112px;top:24px;width:320px;font-size:7.4px;line-height:11.5px;color:#555}
.p-link{position:absolute;left:112px;top:70px;font-size:7.5px;color:var(--blue)}
.price{position:absolute;left:463px;top:0;width:114px;height:85px}
.price .amt{position:absolute;left:20px;right:0;top:0;height:85px;color:#fff;font-weight:600;text-align:center}
.price .old{position:absolute;left:0;right:0;top:8px;font-size:13.5px;text-decoration:line-through;color:#5a2a00;opacity:.7}
.price .val{position:absolute;left:0;right:0;top:27px;font-size:27px;line-height:1}
.price .val.mid{top:28px}
.price .book{position:absolute;left:18px;width:60px;bottom:0;height:14px;font-size:8.5px;line-height:14px;border-radius:3px 3px 0 0;font-weight:700}
.footer{left:0;top:1052px;width:1068px;height:116px;background:#f4f4f4;border-top:1px solid var(--line)}
.f-col{top:1062px}
.f-col h4{font-weight:400;font-size:13.5px;color:#333;margin-bottom:24px}
.f-col ul{list-style:none;font-size:7.8px;line-height:19px;color:#333}
.f-col li.b:before{content:"•";margin-right:7px}
.f-row{display:flex}
.f-row span:first-child{width:30px}
.f-row span:nth-child(2){width:30px}
.news p{font-size:7.8px;line-height:13px;width:205px;color:#333;margin-top:-4px}
.news .in{display:flex;gap:8px;margin-top:6px}
.news .in div:first-child{width:138px;height:15px;border:1px solid #ccc;border-radius:3px;background:#fff;font-size:7.5px;padding-left:6px;line-height:13px}
.news .in div:last-child{width:30px;height:15px;border-radius:3px;background:linear-gradient(#a9adb1,#7f8489);color:#fff;text-align:center;font-size:12px;line-height:15px}
.bottom{left:0;top:1168px;width:1068px;height:28px;background:#ececec;font-size:7.8px;color:#333}
.bottom span{position:absolute;left:162px;top:10px}
.social{position:absolute;left:811px;top:3px;display:flex;gap:8px}
.social i{width:18px;height:18px;border-radius:2px}
.endline{left:0;top:1196px;width:1068px;height:4px;background:#a8a8a8}
</style>
</head>
<body>
<div class="page">
  <div class="abs topline"></div>
  <header class="abs header"></header>
  <div class="abs brand">HOPLY<span class="brand-dot"></span></div>
  <div class="abs brand-sub">Trampolines</div>
  <div class="abs call">
    <svg width="8" height="18" viewBox="0 0 8 18"><path d="M6 1C2 1 1 5 1 9s1 8 5 8" fill="none" stroke="#444" stroke-width="3" stroke-linecap="round"/></svg>
    <div>CALL US TODAY<br>(84) - 555 010 010</div>
  </div>
  <div class="abs lang"><span class="flag"></span>En ▾<span class="sep"></span>USD ▾</div>
  <div class="abs btn-sm" style="left:669px;width:55px">Login</div>
  <div class="abs btn-sm" style="left:737px;width:55px">Register</div>
  <div class="abs search">Search....
    <svg width="9" height="9" viewBox="0 0 10 10"><circle cx="4" cy="4" r="3" fill="none" stroke="#fff" stroke-width="1.3"/><path d="M6.3 6.3L9 9" stroke="#fff" stroke-width="1.3"/></svg>
  </div>
  <nav class="abs nav">
    <a>HOME</a><a>BOOK NOW</a><a>ABOUT US</a><a>LOCATIONS &amp; HOURS</a><a>JUMPING</a><a>GROUPS &amp; EVENTS</a><a>GALLERY</a><a>SAFETY</a><a>LATEST NEWS</a><a>CAREERS</a>
  </nav>

  <div class="abs side-head" style="top:150px">Availability Check</div>
  <div class="abs side-box" style="top:191px;height:147px">
    <div class="cal-title"><span style="left:9px">◂</span>March 2014<span style="right:9px">▸</span></div>
    <table class="cal">
      <tr><th>SUN</th><th>MON</th><th>TUE</th><th>WED</th><th>THU</th><th>FRI</th><th>SAT</th></tr>
      <tr><td class="o">28</td><td class="o">29</td><td class="o">30</td><td class="o">31</td><td>1</td><td>2</td><td>3</td></tr>
      <tr><td>4</td><td>5</td><td>6</td><td>7</td><td>8</td><td>9</td><td>10</td></tr>
      <tr><td>11</td><td>12</td><td>13</td><td>14</td><td>15</td><td>16</td><td>17</td></tr>
      <tr><td>18</td><td>19</td><td>20</td><td>21</td><td>22</td><td>23</td><td>24</td></tr>
      <tr><td>25</td><td>26</td><td>27</td><td>28</td><td>29</td><td>30</td><td>31</td></tr>
    </table>
  </div>
  <div class="abs side-head" style="top:351px">My Basket</div>
  <div class="abs side-box basket" style="top:391px;height:84px">No Products in the cart.</div>
  <div class="abs side-head" style="top:487px">Area We Cover</div>
  <div class="abs side-box area" style="top:528px;height:277px">
    Lorem Ipsum is simply dummy text of the printing and typesetting industry. Lorem Ipsum has been the industry's standard dummy text ever since the 1500s, when an unknown printer took a galley of type and scrambled it to make a type specimen book. It has survived not only five centuries, but also the leap into electronic typesetting, remaining essentially unchanged. It was popularised in the 1960s with the release of Letraset sheets containing Lorem Ipsum passages, and more recently with desktop publishing software like Aldus PageMaker including versions of Lorem Ipsum.
    <span class="view-map">View Map</span>
  </div>

  <section class="abs slider">
    <div class="slider-art" role="img" aria-label="Trampoline with safety net enclosure and ladder"></div>
    <div class="tag tag1">Finally, a <b>Springless</b></div>
    <div class="tag tag2"><b>Trampoline</b> that won't</div>
    <div class="tag tag3">Break the bank.</div>
    <div class="arrow" style="left:12px"><svg width="8" height="10"><path d="M6 1L2 5l4 4" fill="none" stroke="#fff" stroke-width="1.8"/></svg></div>
    <div class="arrow" style="left:540px"><svg width="8" height="10"><path d="M2 1l4 4-4 4" fill="none" stroke="#fff" stroke-width="1.8"/></svg></div>
    <div class="dots"><i></i><i class="on"></i><i></i></div>
  </section>

  <div class="abs toolbar">
    Page 01 of 06
    <div class="pager"><span>‹</span><span class="cur">01</span><span>02</span><span>03</span><span>04</span><span>›</span></div>
    <span class="sort">Short by :</span>
    <div class="select">Availability</div>
    <div class="toggle">List<div class="track"><i></i></div>Map</div>
  </div>
  <div class="abs product-rule" style="top:422px"></div>

  <div class="abs product" style="top:441px">
    <div class="thumb"><div role="img" aria-label="Rectangular 8 x 12ft trampoline"></div></div>
    <div class="p-name">RECTANGULAR 8 X 12FT TRAMPOLINE</div>
    <div class="p-desc">Lorem Ipsum is simply dummy text of the printing and typesetting industry. Lorem Ipsum has been the industry's standard dummy text ever since the 1500s, when an unknown printer took a galley of type and scrambled it to make a type specimen book.</div>
    <div class="p-link">View Details &gt;&gt;</div>
    <div class="price"><svg class="abs" width="24" height="85" style="left:0;top:0"><path d="M20 0L0 42l20 43z" fill="var(--orange-dark)"/></svg>
      <div class="amt" style="background:var(--orange)"><div class="old">$600</div><div class="val">$500</div><div class="book" style="background:var(--orange-dark);color:#fff">BOOK</div></div></div>
  </div>
  <div class="abs product-rule" style="top:545px"></div>

  <div class="abs product" style="top:564px">
    <div class="thumb"><div role="img" aria-label="Classic 16ft round trampoline"></div></div>
    <div class="p-name">CLASSIC 16FT TRAMPOLINE</div>
    <div class="p-desc">Lorem Ipsum is simply dummy text of the printing and typesetting industry. Lorem Ipsum has been the industry's standard dummy text ever since the 1500s, when an unknown printer took a galley of type and scrambled it to make a type specimen book.</div>
    <div class="p-link">View Details &gt;&gt;</div>
    <div class="price"><svg class="abs" width="24" height="85" style="left:0;top:0"><path d="M20 0L0 42l20 43z" fill="var(--blue-dark)"/></svg>
      <div class="amt" style="background:var(--blue)"><div class="val mid">$400</div><div class="book" style="background:#0c5f86;color:#fff">BOOK</div></div></div>
  </div>
  <div class="abs product-rule" style="top:668px"></div>

  <div class="abs product" style="top:688px">
    <div class="thumb"><div role="img" aria-label="Classic 15ft trampoline"></div></div>
    <div class="p-name">CLASSIC 15FT TRAMPOLINE</div>
    <div class="p-desc">Lorem Ipsum is simply dummy text of the printing and typesetting industry. Lorem Ipsum has been the industry's standard dummy text ever since the 1500s, when an unknown printer took a galley of type and scrambled it to make a type specimen book.</div>
    <div class="p-link">View Details &gt;&gt;</div>
    <div class="price"><svg class="abs" width="24" height="85" style="left:0;top:0"><path d="M20 0L0 42l20 43z" fill="var(--grey-dark)"/></svg>
      <div class="amt" style="background:var(--grey)"><div class="val mid">$350</div><div class="book" style="background:#6b6b6b;color:#fff">BOOK</div></div></div>
  </div>
  <div class="abs product-rule" style="top:791px"></div>

  <div class="abs product" style="top:811px">
    <div class="thumb"><div role="img" aria-label="Octagonal 14ft trampoline"></div></div>
    <div class="p-name">OCTAGONAL 14FT TRAMPOLINE</div>
    <div class="p-desc">Lorem Ipsum is simply dummy text of the printing and typesetting industry. Lorem Ipsum has been the industry's standard dummy text ever since the 1500s, when an unknown printer took a galley of type and scrambled it to make a type specimen book.</div>
    <div class="p-link">View Details &gt;&gt;</div>
    <div class="price"><svg class="abs" width="24" height="85" style="left:0;top:0"><path d="M20 0L0 42l20 43z" fill="var(--orange-dark)"/></svg>
      <div class="amt" style="background:var(--orange)"><div class="val mid">$300</div><div class="book" style="background:var(--orange-dark);color:#fff">BOOK</div></div></div>
  </div>
  <div class="abs product-rule" style="top:915px"></div>

  <div class="abs product" style="top:934px">
    <div class="thumb"><div role="img" aria-label="Rectangular 7 x 10ft trampoline"></div></div>
    <div class="p-name">RECTANGULAR 7 X 10FT TRAMPOLINE</div>
    <div class="p-desc">Lorem Ipsum is simply dummy text of the printing and typesetting industry. Lorem Ipsum has been the industry's standard dummy text ever since the 1500s, when an unknown printer took a galley of type and scrambled it to make a type specimen book.</div>
    <div class="p-link">View Details &gt;&gt;</div>
    <div class="price"><svg class="abs" width="24" height="85" style="left:0;top:0"><path d="M20 0L0 42l20 43z" fill="var(--blue-dark)"/></svg>
      <div class="amt" style="background:var(--blue)"><div class="val mid">$250</div><div class="book" style="background:#0c5f86;color:#fff">BOOK</div></div></div>
  </div>

  <footer class="abs footer"></footer>
  <div class="abs f-col" style="left:180px">
    <h4>Contact us</h4>
    <ul>
      <li class="f-row"><span>Tell</span><span>:</span><span>00 000 000 000</span></li>
      <li class="f-row"><span>Email</span><span>:</span><span style="color:var(--blue)">contact@hoplyjump.com</span></li>
      <li class="f-row"><span>Add</span><span>:</span><span>Street, Riverside City, Vn</span></li>
    </ul>
  </div>
  <div class="abs f-col" style="left:353px">
    <h4>Support &amp; Help</h4>
    <ul><li class="b">Payment Options</li><li class="b">FAQ</li><li class="b">Privacy &amp; Policy</li></ul>
  </div>
  <div class="abs f-col" style="left:526px">
    <h4>Information</h4>
    <ul><li class="b">My Account</li><li class="b">Sit Map</li><li class="b">Order History</li></ul>
  </div>
  <div class="abs f-col news" style="left:700px">
    <h4>Newsletter</h4>
    <p>Lorem Ipsum is simply dummy text of the printing and typesetting industry.</p>
    <div class="in"><div>Enter your email......</div><div>+</div></div>
  </div>
  <div class="abs bottom"><span>©2014 Hoply. All rights reserved.</span>
    <div class="social"><i style="background:#3b5a9a"></i><i style="background:#2aa9e0"></i><i style="background:#1a7bb9"></i><i style="background:#d64a3a"></i></div>
  </div>
  <div class="abs endline"></div>
</div>
</body>
</html>
```